Coffee House With Cycling Theme Wants Business Cards

We want to create a business card for a coffee house that has a cycling theme. We expect to use the current logo on one side of the business card and we have been considering adding the words 'COFFEE HOUSE' underneath (see example). For the other side of the business card we want an interesting design with tag-line, address and social media links (the normal business card stuff). See examples provided but we are not fixed on having it exactly as shown, we are very open to great creative ideas. Please note our logo has the initials ‘RV' in orange embedded in the design and this must be retained. However, you can play with the words COFFEE HOUSE as well as use the orange color on the backside of the business card, as you see fit. For an image on the backside of the business card it can be a photo, hand-drawn or whatever but it must visually combine coffee and cycling in some way. The interior of the Coffee House will be reclaimed wood, rustic and have an urban feel to it with cycling artifacts hanging from the walls/ceiling, etc. Finally, it would be beneficial if the business card design elements can be easily used on flyers and other promotional assets. Good luck, we are looking forward to seeing your creative ideas.

Target Market(s)

Coffee lovers and cycling fans

Contact Information for Business Card

See project description.

Colors

Designer to choose colors to be used in the design.

Requirements
Must have
• Must use the current logo provided and combine a coffee and bike theme.
Nice to have
• Orange is used in current logo and could be used as an accent color on the backside of the business card.

```html
<!DOCTYPE html>
<html lang="en">
<head>
<meta charset="utf-8">
<title>RV Coffee House – Business Card</title>
<link rel="stylesheet" href="https://fonts.googleapis.com/css2?family=Fira+Sans:wght@500;600&family=Montserrat:wght@700&display=swap">
<style>
  :root {
    --orange: #ee6a28;
    --charcoal: #3d3d3d;
    --card: #ffffff;
    --backdrop: #e9e6e2;
  }
  * { box-sizing: border-box; margin: 0; padding: 0; }
  html, body { width: 1154px; height: 1200px; overflow: hidden; }
  body {
    background: var(--backdrop);
    position: relative;
    font-family: "Fira Sans", sans-serif;
    color: var(--charcoal);
  }
  .card {
    position: absolute;
    left: 100px;
    width: 954px;
    height: 520px;
    background: var(--card);
    border-radius: 26px;
    box-shadow: 0 6px 18px rgba(0,0,0,.18);
    overflow: hidden;
  }
  .card--front { top: 40px; }
  .card--back { top: 620px; }

  /* Front */
  .wordmark {
    position: absolute;
    inset: 0;
    display: flex;
    align-items: center;
    justify-content: center;
    gap: 36px;
  }
  .wordmark__dot {
    width: 120px; height: 120px;
    border-radius: 50%;
    background: var(--orange);
    flex: none;
  }
  .wordmark__name {
    font-family: "Montserrat", sans-serif;
    font-weight: 700;
    color: var(--charcoal);
    line-height: .95;
    text-transform: uppercase;
  }
  .wordmark__initials { display: block; font-size: 150px; }
  .wordmark__words { display: block; font-size: 72px; letter-spacing: 1px; }

  /* Back */
  .stripe { position: absolute; top: 0; bottom: 0; width: 12px; }
  .stripe--orange { left: 14px; background: var(--orange); }
  .stripe--charcoal { left: 46px; background: var(--charcoal); }

  .back__content {
    position: absolute;
    left: 80px; right: 110px; top: 0; bottom: 0;
    display: flex;
    flex-direction: column;
    align-items: center;
    text-align: center;
  }
  .tagline {
    margin-top: 100px;
    font-weight: 600;
    font-size: 37px;
    letter-spacing: .2px;
  }
  .tagline__stop { color: var(--orange); }
  .address {
    margin-top: 18px;
    font-weight: 500;
    font-size: 21px;
  }
  .address__sep { color: var(--orange); margin: 0 8px; }

  .mini-mark {
    margin-top: 58px;
    display: flex;
    align-items: center;
    gap: 12px;
    font-family: "Montserrat", sans-serif;
    font-weight: 700;
    text-transform: uppercase;
    line-height: .95;
    color: var(--charcoal);
  }
  .mini-mark__dot { width: 34px; height: 34px; border-radius: 50%; background: var(--orange); }
  .mini-mark__name { text-align: left; }
  .mini-mark__initials { display: block; font-size: 40px; }
  .mini-mark__words { display: block; font-size: 18px; }

  .contacts {
    margin-top: 56px;
    display: flex;
    gap: 56px;
    font-weight: 500;
    font-size: 24px;
  }
  .contact { display: flex; align-items: center; gap: 8px; }
  .contact__dot {
    width: 26px; height: 26px;
    border-radius: 50%;
    border: 2.5px solid var(--orange);
  }
  .contact svg { width: 28px; height: 28px; }

  .bike-strip {
    position: absolute;
    right: 14px; top: 10px; bottom: 10px;
    width: 80px;
    background: linear-gradient(180deg, #d9d9d9, #bdbdbd);
    border-radius: 14px;
  }
</style>
</head>
<body>

<section class="card card--front" aria-label="Business card front">
  <div class="wordmark">
    <span class="wordmark__dot"></span>
    <h1 class="wordmark__name">
      <span class="wordmark__initials">RV</span>
      <span class="wordmark__words">Coffee House</span>
    </h1>
  </div>
</section>

<section class="card card--back" aria-label="Business card back">
  <span class="stripe stripe--orange"></span>
  <span class="stripe stripe--charcoal"></span>

  <div class="back__content">
    <p class="tagline">a great day starts with coffee and a ride<span class="tagline__stop">.</span></p>
    <p class="address">48 Spoke Lane<span class="address__sep">•</span>Millbrook<span class="address__sep">•</span>State</p>

    <div class="mini-mark">
      <span class="mini-mark__dot"></span>
      <span class="mini-mark__name">
        <span class="mini-mark__initials">RV</span>
        <span class="mini-mark__words">Coffee House</span>
      </span>
    </div>

    <div class="contacts">
      <span class="contact"><span class="contact__dot"></span>@rvcoffeehouse</span>
      <span class="contact">
        <svg viewBox="0 0 28 28" aria-hidden="true">
          <g fill="none" stroke="var(--orange)" stroke-width="2.2">
            <circle cx="14" cy="14" r="11"/>
            <ellipse cx="14" cy="14" rx="5" ry="11"/>
            <line x1="3" y1="14" x2="25" y2="14"/>
            <line x1="5" y1="8.5" x2="23" y2="8.5"/>
            <line x1="5" y1="19.5" x2="23" y2="19.5"/>
          </g>
        </svg>
        www.rvcoffeehouse.com
      </span>
    </div>
  </div>

  <div class="bike-strip" role="img" aria-label="Vertical pattern of line-drawn bicycles alternating with steaming coffee cups"></div>
</section>

</body>
</html>
```